Powerpoint Template needed for new Digital Consultancy

We have recently had our logo designed through Sketchmarket and would now like to extend the brand look & feel through to having a powerpoint template created that we can use as a master template within which to create our client presentations.
Typical slides required and in terms of what we would need templating is:

- Stylised header and footer for main content slides
- intro/front page slide
- contents page slide
- standardised font type and sizes, heading types (including sizes) for Level 1, Level 2 and Level 3 headings
- use of text colour and any standards/styling around when to use bold, underline, italics etc
- table styling for when we want to use tables in the presentation
- standards and styles around using bullet and number lists
- stylising use of imagery that is dropped in e.g. do all images have a certain border style or drop-shadow etc.
- style and slide layout/format for how team profiles are handled
- style and slide layout/format for how case studies are handled
- closing, contact-us page

We can send over logo files and colour/font styles etc used for the logo soon.

Target Market(s)

B2B professional clients that are either medium to large corporations or potentially some government departments.

Industry/Entity Type

Digital

Font styles to use
Sans Serif

Colors
ec1f27
f37122
f78f20
faa54b
f68d4d
0255a3

Requirements
Must have
• Ideally as many templated pages/master slide types as outlined above in the brief to meet the requirements of what the powerpoint deck will be used for. Namely client presentations and pitches.
• Versions of the logo are attached to give an idea of the colour palette and clean, modern style we are looking for, plus the type of font we are using and like.
• We are looking for the slide design to be modern, minimalistic, clean and not overuse of colour. Preferably a white slide background so it's easy to then read slide content when we populate the slides with text which will be in black.
Nice to have
• Not expecting to see too much more than simple use of the logo and a slide header perhaps using some sort of line as a break and then a simple footer as well.
• Consider using Abode font.
Should not have
• Too much block colour or elements that draw away from what will go in the main content body of our slides when we use them.

```html
<!DOCTYPE html>
<html lang="en">
<head>
<meta charset="utf-8">
<title>brightloop – Slide Master Set</title>
<link rel="stylesheet" href="https://fonts.googleapis.com/css2?family=Open+Sans:wght@300;400;600&display=swap">
<style>
  :root {
    --brand-blue: #0255a3;
    --brand-red: #ec1f27;
    --brand-orange: #f37122;
    --brand-amber: #f78f20;
    --icon-gold: #f0b400;
    --icon-grey: #666666;
    --text-grey: #7a7a7a;
    --spoke-grey: #efefef;
    --canvas: #ffffff;
  }
  * { box-sizing: border-box; margin: 0; padding: 0; }
  html, body { width: 1200px; height: 681px; overflow: hidden; background: var(--canvas); }
  body { position: relative; font-family: "Open Sans", Arial, sans-serif; }

  .slide { position: absolute; overflow: hidden; background: var(--canvas); }
  .slide--two-col { left: 0; top: 16px; width: 564px; height: 323px; }
  .slide--four-col { left: 636px; top: 16px; width: 564px; height: 323px; }
  .slide--process { left: 0; top: 355px; width: 564px; height: 326px; }
  .slide--closing { left: 640px; top: 363px; width: 560px; height: 318px; }

  .slide-header {
    position: absolute; left: 0; top: 0; width: 100%; height: 33px;
    background: var(--brand-blue);
    display: flex; align-items: center; gap: 6px; padding-left: 4px;
  }
  .slide-header__title { color: var(--brand-red); font-size: 20px; font-weight: 400; }
  .ring { width: 22px; height: 22px; border: 2px solid var(--brand-red); border-radius: 50%; flex: none; }
  .ring--small { width: 16px; height: 16px; border-width: 1.5px; border-color: #3a78c0; }

  .section-bar {
    position: absolute; width: 240px; height: 25px; background: var(--brand-blue);
    display: flex; align-items: center; gap: 8px; padding-left: 6px;
  }
  .section-bar__title { color: var(--brand-amber); font-size: 12px; font-weight: 400; }

  .bullets { position: absolute; list-style: none; color: var(--text-grey); font-size: 11.5px; font-weight: 300; }
  .bullets li { height: 16px; line-height: 16px; display: flex; align-items: center; }
  .bullets li::before {
    content: ""; width: 5px; height: 5px; border: 1px solid var(--brand-red);
    border-radius: 50%; margin-right: 5px;
  }
  .bullets .lvl-2 { padding-left: 21px; }
  .bullets .lvl-3 { padding-left: 42px; }
  .bullets .lvl-3::before { border-color: var(--brand-amber); }

  .footer-brand {
    position: absolute; display: flex; align-items: center; gap: 3px;
    color: var(--brand-red); font-size: 9px; font-weight: 400;
  }
  .footer-brand .dot { width: 9px; height: 9px; border: 1.2px solid var(--brand-red); border-radius: 50%; }

  .process-label { position: absolute; font-size: 7.5px; line-height: 12px; color: #333; width: 100px; }
  .process-label--right { text-align: right; }

  .closing-backdrop {
    position: absolute; inset: 0;
    background: radial-gradient(circle at 50% 45%, #ffffff 0%, #f4f4f4 60%, #e9e9e9 100%);
  }
  .closing-mark {
    position: absolute; left: 252px; top: 100px; width: 56px; height: 56px;
    border: 3px solid var(--brand-red); border-radius: 50%;
  }
  .closing-brand {
    position: absolute; left: 0; right: 0; top: 168px; text-align: center;
    color: var(--brand-red); font-size: 37px; font-weight: 400; line-height: 1;
  }
  .closing-thanks {
    position: absolute; left: 0; right: 0; top: 216px; text-align: center;
    color: var(--brand-red); font-size: 34px; font-weight: 300; line-height: 1;
  }
</style>
</head>
<body>

<section class="slide slide--two-col">
  <header class="slide-header"><span class="ring"></span><h1 class="slide-header__title">Difference Between or Comparative</h1></header>
  <div class="section-bar" style="left:39px;top:39px"><span class="ring ring--small"></span><span class="section-bar__title">Title</span></div>
  <div class="section-bar" style="left:286px;top:39px"><span class="ring ring--small"></span><span class="section-bar__title">Title</span></div>
  <ul class="bullets" style="left:44px;top:84px"><li>Fist level bullet</li><li class="lvl-2">Second level bullet</li><li class="lvl-3">Third level bullet</li></ul>
  <ul class="bullets" style="left:291px;top:84px"><li>Fist level bullet</li><li class="lvl-2">Second level bullet</li><li class="lvl-3">Third level bullet</li></ul>
  <div class="footer-brand" style="left:470px;top:290px"><span class="dot"></span>brightloop</div>
</section>

<section class="slide slide--four-col">
  <header class="slide-header"><span class="ring"></span><h1 class="slide-header__title">Difference Between or Comparative</h1></header>
  <div class="section-bar" style="left:39px;top:39px"><span class="ring ring--small"></span><span class="section-bar__title">Title</span></div>
  <div class="section-bar" style="left:286px;top:39px"><span class="ring ring--small"></span><span class="section-bar__title">Title</span></div>
  <ul class="bullets" style="left:44px;top:84px"><li>Fist level bullet</li><li class="lvl-2">Second level bullet</li><li class="lvl-3">Third level bullet</li></ul>
  <ul class="bullets" style="left:291px;top:84px"><li>Fist level bullet</li><li class="lvl-2">Second level bullet</li><li class="lvl-3">Third level bullet</li></ul>
  <div class="section-bar" style="left:39px;top:154px"><span class="ring ring--small"></span><span class="section-bar__title">Title</span></div>
  <div class="section-bar" style="left:286px;top:154px"><span class="ring ring--small"></span><span class="section-bar__title">Title</span></div>
  <ul class="bullets" style="left:44px;top:199px"><li>Fist level bullet</li><li class="lvl-2">Second level bullet</li><li class="lvl-3">Third level bullet</li></ul>
  <ul class="bullets" style="left:291px;top:199px"><li>Fist level bullet</li><li class="lvl-2">Second level bullet</li><li class="lvl-3">Third level bullet</li></ul>
  <div class="footer-brand" style="left:470px;top:290px"><span class="dot"></span>brightloop</div>
</section>

<section class="slide slide--process">
  <svg width="564" height="326" viewBox="0 0 564 326" aria-hidden="true">
    <g class="spokes" fill="var(--spoke-grey)">
      <rect x="261" y="50" width="46" height="232"/>
      <rect x="261" y="50" width="46" height="232" transform="rotate(60 284 166)"/>
      <rect x="261" y="50" width="46" height="232" transform="rotate(-60 284 166)"/>
    </g>
    <g class="spoke-edges" fill="#b5b5b5">
      <rect x="208" y="152" width="10" height="28"/><rect x="350" y="152" width="10" height="28"/>
      <polygon points="240,112 260,102 260,120"/><polygon points="328,112 308,102 308,120"/>
      <polygon points="240,222 260,232 260,214"/><polygon points="328,222 308,232 308,214"/>
    </g>
    <circle class="hub" cx="284" cy="166" r="42" fill="#fff" stroke="var(--icon-gold)" stroke-width="3"/>
    <g class="pointers" fill="var(--icon-gold)">
      <polygon points="276,77 292,77 284,87"/><polygon points="276,255 292,255 284,245"/>
      <polygon points="172,108 186,112 178,122"/><polygon points="390,108 376,112 384,122"/>
      <polygon points="172,222 186,218 178,208"/><polygon points="392,222 378,218 386,208"/>
    </g>
    <g class="nodes" fill="#fff" stroke="var(--icon-gold)" stroke-width="3">
      <circle cx="284" cy="49" r="30"/><circle cx="150" cy="89" r="30"/><circle cx="412" cy="89" r="30"/>
      <circle cx="150" cy="241" r="30"/><circle cx="414" cy="241" r="30"/><circle cx="284" cy="283" r="30"/>
    </g>
    <g class="icons" fill="var(--icon-grey)">
      <!-- handshake -->
      <path d="M272 54 l8 -10 l6 2 l10 -6 l3 4 l-9 8 l-4 0 l-8 9 z"/>
      <path d="M276 58 l4 4 M280 55 l4 4" stroke="#fff" stroke-width="1.5"/>
      <!-- price tag with coin -->
      <path d="M141 80 l10 -4 l12 12 l-9 9 l-12 -12 z"/>
      <circle cx="146" cy="81" r="1.5" fill="#fff"/>
      <text x="151" y="92" font-size="9" font-family="Open Sans, sans-serif" font-weight="600" fill="#fff">$</text>
      <circle cx="163" cy="97" r="2.5"/><rect x="160" y="100" width="6" height="4" rx="1"/>
      <!-- piggy bank -->
      <ellipse cx="411" cy="92" rx="11" ry="8"/>
      <rect x="404" y="97" width="3" height="5"/><rect x="414" y="97" width="3" height="5"/>
      <rect x="421" y="89" width="3" height="5" rx="1"/>
      <circle cx="414" cy="78" r="4" fill="none" stroke="var(--icon-grey)" stroke-width="1.2"/>
      <!-- umbrella -->
      <path d="M139 241 a11 11 0 0 1 22 0 z"/><path d="M150 241 v9 a2 2 0 0 1 -4 0" fill="none" stroke="var(--icon-grey)" stroke-width="2"/>
      <!-- calculator -->
      <rect x="406" y="230" width="16" height="22" rx="2" transform="rotate(-12 414 241)"/>
      <g fill="#fff" transform="rotate(-12 414 241)">
        <rect x="409" y="233" width="10" height="4"/>
        <rect x="409" y="240" width="2.5" height="2.5"/><rect x="413" y="240" width="2.5" height="2.5"/><rect x="417" y="240" width="2.5" height="2.5"/>
        <rect x="409" y="245" width="2.5" height="2.5"/><rect x="413" y="245" width="2.5" height="2.5"/><rect x="417" y="245" width="2.5" height="2.5"/>
      </g>
      <!-- house -->
      <path d="M273 292 v-10 l11 -9 l11 9 v10 h-7 v-7 h-8 v7 z"/>
    </g>
  </svg>
  <p class="process-label" style="left:325px;top:25px">Lorem Ipsum is simply<br>dummy text.</p>
  <p class="process-label process-label--right" style="left:5px;top:73px">Lorem Ipsum is simply<br>dummy text.</p>
  <p class="process-label" style="left:455px;top:73px">Lorem Ipsum is simply<br>dummy text.</p>
  <p class="process-label process-label--right" style="left:5px;top:230px">Lorem Ipsum is simply<br>dummy text.</p>
  <p class="process-label" style="left:455px;top:230px">Lorem Ipsum is simply<br>dummy text.</p>
  <p class="process-label" style="left:325px;top:283px">Lorem Ipsum is simply<br>dummy text.</p>
  <div class="footer-brand" style="left:472px;top:302px"><span class="dot"></span>brightloop</div>
</section>

<section class="slide slide--closing">
  <div class="closing-backdrop" role="img" aria-label="Soft white background of embossed circles"></div>
  <div class="closing-mark"></div>
  <p class="closing-brand">brightloop</p>
  <p class="closing-thanks">Thank You</p>
</section>

</body>
</html>
```